Dean Hollis Business Card

In addition to my name design (file uploaded), black print on white card stock, e-mail address should be presented as a typical e-mail address, i.e., underlined and in blue ink, the card should include the following information:
Professor of Aviation Technology
Accident Litigation Expert Witness
Master Certificated Flight Instructor

dhollis@vexmail.example
Anchorage, Alaska
(907) 318-5074

```html
<!DOCTYPE html>
<html lang="en">
<head>
<meta charset="utf-8">
<title>Dean Hollis Business Card</title>
<link rel="stylesheet" href="https://fonts.googleapis.com/css2?family=Exo+2:wght@400;500&family=Roboto+Condensed:wght@700&display=swap">
<style>
  :root {
    --backdrop: #e4e4e4;
    --card: #ffffff;
    --ink: #1e1e1e;
    --ink-soft: #333333;
    --link: #1a4fb5;
    --swoosh-dark: #2b2b2b;
    --swoosh-grey: #9a9a9a;
    --swoosh-grey-light: #d2d2d2;
  }
  html, body {
    margin: 0;
    width: 1200px;
    height: 900px;
    overflow: hidden;
    background: var(--backdrop);
  }
  .card {
    position: absolute;
    left: 150px;
    top: 190px;
    width: 900px;
    height: 520px;
    background: var(--card);
    overflow: hidden;
    box-shadow: 0 10px 30px rgba(0,0,0,0.12);
  }
  .card__swoosh {
    position: absolute;
    inset: 0;
    width: 900px;
    height: 520px;
  }
  .card__wordmark {
    position: absolute;
    left: 70px;
    top: 225px;
    margin: 0;
    font-family: "Roboto Condensed", sans-serif;
    font-weight: 700;
    font-size: 84px;
    line-height: 0.92;
    letter-spacing: 2px;
    color: var(--ink);
    text-transform: uppercase;
  }
  .card__wordmark span { display: block; }
  .card__contact {
    position: absolute;
    right: 60px;
    top: 40px;
    text-align: right;
    font-family: "Exo 2", sans-serif;
    color: var(--ink);
  }
  .contact__titles {
    list-style: none;
    margin: 0;
    padding: 0;
    font-size: 19px;
    line-height: 1.35;
    color: var(--ink-soft);
  }
  .contact__titles li:first-child {
    font-size: 21px;
    font-weight: 500;
    color: var(--ink);
  }
  .contact__address {
    margin: 26px 0 0;
    font-size: 19px;
    font-style: normal;
    line-height: 1.25;
    letter-spacing: 0.5px;
  }
  .contact__list {
    list-style: none;
    margin: 22px 0 0;
    padding: 0;
    font-size: 18px;
    line-height: 1.6;
    letter-spacing: 0.5px;
  }
  .contact__list li {
    display: flex;
    justify-content: flex-end;
    align-items: center;
    gap: 10px;
  }
  .contact__email {
    color: var(--link);
    text-decoration: underline;
  }
  .contact__icon {
    width: 16px;
    height: 16px;
    flex: none;
  }
</style>
</head>
<body>
  <main class="card">
    <svg class="card__swoosh" viewBox="0 0 900 520" aria-hidden="true">
      <defs>
        <linearGradient id="greyBand" x1="0" y1="1" x2="1" y2="0">
          <stop offset="0" stop-color="var(--swoosh-grey)"/>
          <stop offset="1" stop-color="var(--swoosh-grey-light)"/>
        </linearGradient>
      </defs>
      <path d="M0,430 Q520,475 900,305 L900,520 L0,520 Z" fill="url(#greyBand)"/>
      <path d="M0,472 Q560,502 900,330 L900,520 L0,520 Z" fill="var(--card)"/>
      <path d="M120,520 Q600,485 900,335 L900,520 Z" fill="var(--swoosh-dark)"/>
      <path d="M330,520 Q690,475 900,375 L900,520 Z" fill="var(--card)"/>
    </svg>

    <h1 class="card__wordmark"><span>Dean E.</span><span>Hollis</span></h1>

    <section class="card__contact">
      <ul class="contact__titles">
        <li>Professor of Aviation Technology</li>
        <li>Accident Litigation Expert Witness</li>
        <li>Master Certificated Flight Instructor</li>
      </ul>
      <address class="contact__address">Anchorage, Alaska</address>
      <ul class="contact__list">
        <li>(907) 318-5074
          <svg class="contact__icon" viewBox="0 0 16 16"><path d="M4 1 L6 5 L4.5 6.5 Q6 10 9.5 11.5 L11 10 L15 12 L13.5 15 Q5 14 1 3 Z" fill="var(--ink)"/></svg>
        </li>
        <li><span class="contact__email">dhollis@vexmail.example</span>
          <svg class="contact__icon" viewBox="0 0 16 16"><rect x="1" y="3" width="14" height="10" fill="var(--ink)"/><path d="M1 3 L8 9 L15 3" fill="none" stroke="var(--card)" stroke-width="1.2"/></svg>
        </li>
      </ul>
    </section>
  </main>
</body>
</html>
```